Velmora Land Surveying Website Design

We are working with Velmora. They are a national land surveying company and in need of a new website design.

Some sites to use for inspiration:

https://brannockeng.com
https://www.qlvinc.com
https://dervanto.com
https://gkw.us
https://corvenbuilt.com
https://www.pellacombwendrix.com

Thank you for taking the time to consider designing a website for us. We are web developers based in Stockton and Los Angeles, CA, USA. Most of our projects go through the same process. Understanding this process may help you win a project with us. We custom-code all of our websites in-house. We don’t have any requirements as to what tools you use for your design, but we prefer Figma files. For any design that we label as four-stars, we send it to the client for review. The client picks the final design they want us to use. Once we complete this process, we will continue to show additional clients all the four-star sites and purchase them later. Your designs will have multiple chances to sell. For better chances of success, we ask that you follow these guidelines.

IMAGES:
If you use any images or icons in the design, we ask that you have a link to the asset so we can purchase the image/icon. Most of the designs we submit do not have the customer’s images on them unless they have some great images. Be creative; show us the feeling you are trying to portray with your image choices. Use any royalty-free site you choose. We subscribe to Quillar and mainly use their images, but we can purchase images outside of Quillar.

PLEASE NOTE: we will not submit designs to clients with watermarks on the images.

FONTS:
We ask that you identify the fonts used in the design. This can be done in a message if you want. We typically use Google Fonts and Quillar Fonts.

CONTENT:
We're always open to different content and ideas. We often submit designs with stock images so the client can see our vision. We typically take pictures after the website launch to use their images with our vision. Lorem Ipsum is fine for paragraphs, but we ask that you write the headers in correct English. We want to be able to show the vision and identify the sections of the website.

INSPIRATION:
We typically add a couple of links in the brief of websites we like to help you get started in your design.

REVISIONS:
We do not often ask for revisions of the designs unless we see something in the design that may not appeal to the client. If there are slight changes that we want to make, we do that in the development process.

FEEDBACK:
We rarely give feedback on designs during the design process. We are working on many website projects and do not have the time to provide feedback. We usually respond if your request is well thought out and asks specific questions, but a note asking “feedback, please” usually goes unanswered.

```html
<!DOCTYPE html>
<html lang="en">
<head>
<meta charset="utf-8">
<title>Velmora Land Surveying</title>
<link href="https://fonts.googleapis.com/css2?family=Rajdhani:wght@600;700&family=Rubik:wght@400;500;600&display=swap" rel="stylesheet">
<style>
:root{
  --red:#e0251b;
  --navy:#0d1628;
  --navy-2:#18233a;
  --ink:#1b1b1f;
  --muted:#8a8d93;
  --gray:#f4f4f4;
  --line:#e4e4e4;
  --white:#ffffff;
  --orange:#f08a24;
}
*{margin:0;padding:0;box-sizing:border-box}
html,body{width:1200px;height:4736px;overflow:hidden;background:var(--white)}
body{font-family:"Rubik",sans-serif;color:var(--ink);position:relative}
.abs{position:absolute}
.head{font-family:"Rajdhani",sans-serif;font-weight:700;color:var(--ink);line-height:1.15}
.eyebrow{font-family:"Rubik",sans-serif;font-size:9px;font-weight:500;color:var(--red);text-transform:uppercase;letter-spacing:.3px}
.center{left:0;width:1200px;text-align:center}
.para{font-size:10px;color:var(--muted);line-height:1.6}
.btn-dark{background:var(--navy);color:var(--white);font-size:9px;font-weight:500;display:flex;align-items:center;justify-content:center}
.photo{position:absolute}
.brand{font-family:"Rajdhani",sans-serif;font-weight:700;color:var(--red);font-size:24px;line-height:.9;display:flex;align-items:center;gap:8px}
.brand small{display:block;font-size:11px;letter-spacing:2px}
.brand .dot{width:34px;height:34px;border-radius:50%;background:var(--red);flex:none}

/* header */
.topbar{left:0;top:0;width:1200px;height:75px;background:var(--white)}
.contact-item{top:24px;display:flex;gap:10px;align-items:center}
.contact-item .ic{width:30px;height:30px;border-radius:50%;background:var(--red);display:flex;align-items:center;justify-content:center}
.contact-item b{display:block;font-size:9px;font-weight:500}
.contact-item span{display:block;font-size:8px;color:var(--muted);margin-top:2px}
.nav{left:0;top:75px;width:1200px;height:43px;background:var(--navy)}
.nav ul{list-style:none;position:absolute;left:244px;top:0;height:43px;display:flex;align-items:center;gap:27px}
.nav li{font-size:8.5px;font-weight:600;color:var(--white);letter-spacing:.4px}
.nav li.active{color:var(--red)}
.nav .tools{position:absolute;right:244px;top:12px;display:flex;gap:14px}
.nav .tools i{width:20px;height:20px;background:var(--navy-2);display:block}

/* hero */
.hero-bg{left:0;top:118px;width:600px;height:468px;background:linear-gradient(180deg,#ffffff,#f7f7f7)}
.hero-photo{left:600px;top:118px;width:600px;height:468px;background:linear-gradient(135deg,#6f7d86 0%,#c9b28c 45%,#e3cfa6 75%,#d8c7a8 100%)}
.play{width:54px;height:54px;border-radius:50%;background:var(--white);display:flex;align-items:center;justify-content:center}
.hero-title{left:244px;top:240px;font-size:48px}
.hero-title em{font-style:normal;color:var(--red)}

/* services */
.services-band{left:0;top:586px;width:1200px;height:287px;background:var(--navy)}
.svc-card{top:746px;width:224px;height:263px;background:var(--white);box-shadow:0 6px 20px rgba(0,0,0,.08);text-align:center}
.svc-card .img{height:105px;background:linear-gradient(160deg,#7a7f78,#b59b3d 50%,#8c9ea8)}
.svc-card .badge{position:absolute;left:90px;top:86px;width:44px;height:44px;border-radius:50%;background:var(--red);border:3px solid var(--white);display:flex;align-items:center;justify-content:center}
.svc-card h3{font-family:"Rajdhani",sans-serif;font-size:14px;margin-top:50px}
.svc-card p{font-size:8.5px;color:var(--muted);line-height:1.6;margin:8px 24px 0}
.svc-card a{display:block;font-size:8px;font-weight:600;color:var(--red);margin-top:10px}

/* about */
.bar-label{left:256px;font-size:9px;font-weight:500;width:327px;display:flex;justify-content:space-between}
.bar{left:256px;width:327px;height:3px;background:var(--line)}
.bar i{display:block;height:3px;background:var(--red)}
.corner{position:absolute;width:30px;height:30px;border-color:var(--orange);border-style:solid;border-width:0}

/* why */
.feature h4{font-family:"Rajdhani",sans-serif;font-size:14px;font-weight:700}
.feature p{font-size:8.5px;color:var(--muted);line-height:1.6;margin-top:8px;width:245px}

/* portfolio */
.proj{top:2226px;width:224px;height:262px;background:linear-gradient(180deg,#5b6777,#3a4658 60%,#2b3444)}
.proj h4{position:absolute;left:18px;top:210px;font-family:"Rajdhani",sans-serif;font-size:14px;color:var(--white)}
.proj span{position:absolute;left:18px;top:232px;font-size:7px;letter-spacing:1px;color:#d9dde2}

/* stats */
.stats{left:0;top:2588px;width:1200px;height:103px;background:var(--red)}
.stat{top:22px;display:flex;gap:10px;align-items:flex-start;color:var(--white)}
.stat b{font-family:"Rajdhani",sans-serif;font-size:36px;line-height:1;display:block}
.stat span{font-size:9px;display:block;margin-top:3px}

/* team */
.member{top:3222px;width:224px;text-align:center}
.member .img{height:241px;background:linear-gradient(180deg,#c8cdd3,#e4a25a 55%,#d86f1e)}
.member h4{font-family:"Rajdhani",sans-serif;font-size:14px;margin-top:18px}
.member span{font-size:8.5px;color:var(--red);display:block;margin-top:4px}
.member i{display:block;height:3px;background:var(--red);margin-top:12px}

/* faq */
.faq{left:612px;width:332px;height:31px;background:var(--white);box-shadow:0 2px 10px rgba(0,0,0,.08);display:flex;align-items:center;justify-content:space-between;padding:0 12px;font-size:8.5px;font-weight:500}
.faq.open{background:var(--navy);color:var(--white)}
.faq .mk{width:18px;height:18px;display:flex;align-items:center;justify-content:center;font-size:13px}
.faq.open .mk{background:var(--red)}

/* blog */
.post{top:3942px;width:224px;height:295px;background:var(--white);box-shadow:0 6px 20px rgba(0,0,0,.08)}
.post .img{height:157px;background:linear-gradient(160deg,#c4c8cc,#d8b04e 55%,#9aa2a8)}
.post .date{position:absolute;left:21px;top:142px;width:33px;height:33px;background:var(--red);color:var(--white);text-align:center;font-family:"Rajdhani",sans-serif;font-size:14px;line-height:1;padding-top:5px}
.post .date small{display:block;font-size:6px;font-family:"Rubik",sans-serif}
.post h4{position:absolute;left:19px;top:202px;font-family:"Rajdhani",sans-serif;font-size:14px;line-height:1.5;width:190px}
.post .meta{position:absolute;left:19px;top:267px;font-size:8px;color:var(--muted);display:flex;align-items:center;gap:4px}
.post .meta svg{flex:none}
.post .meta .gap{width:10px}
.partner{top:4296px;width:40px;height:36px;border:3px solid #3a4153;border-radius:4px}

/* footer */
.footer{left:0;top:4391px;width:1200px;height:345px;background:var(--navy);color:var(--white)}
.footer h5{font-family:"Rajdhani",sans-serif;font-size:16px;font-weight:700;position:absolute;top:53px}
.flinks{position:absolute;list-style:none;top:96px}
.flinks li{font-size:9px;font-weight:500;height:24.5px}
.flinks li::before{content:"›";color:var(--red);margin-right:6px}
.fpost{position:absolute;left:608px;display:flex;gap:8px}
.fpost i{width:40px;height:40px;background:linear-gradient(160deg,#9aa2a8,#d8b04e);display:block;flex:none}
.fpost b{font-size:8.5px;font-weight:500;line-height:1.35;display:block;width:120px}
.fpost span{font-size:7px;color:var(--red)}
.finfo{position:absolute;left:790px;font-size:8.5px;line-height:1.6;display:flex;gap:10px}
.finfo .pin{width:10px;height:10px;flex:none;margin-top:2px}
</style>
</head>
<body>

<!-- header -->
<header class="abs topbar">
  <div class="abs brand" style="left:244px;top:14px">
    <span class="dot"></span>
    <span>VELMORA<small>LAND SURVEYING</small></span>
  </div>
  <div class="abs contact-item" style="left:552px">
    <span class="ic"><svg width="13" height="13" viewBox="0 0 24 24"><path fill="#fff" d="M6.6 10.8c1.4 2.8 3.8 5.1 6.6 6.6l2.2-2.2c.3-.3.7-.4 1-.2 1.1.4 2.3.6 3.6.6.6 0 1 .4 1 1V20c0 .6-.4 1-1 1C10.6 21 3 13.4 3 4c0-.6.4-1 1-1h3.5c.6 0 1 .4 1 1 0 1.3.2 2.5.6 3.6.1.3 0 .7-.2 1l-2.3 2.2z"/></svg></span>
    <div><b>Call Now</b><span>(+1) 555.014.2286</span></div>
  </div>
  <div class="abs contact-item" style="left:686px">
    <span class="ic"><svg width="13" height="13" viewBox="0 0 24 24"><path fill="#fff" d="M3 5h18v14H3z M3 5l9 7 9-7" stroke="#e0251b" stroke-width="1.5"/></svg></span>
    <div><b>Email</b><span>hello@velmoraland.com</span></div>
  </div>
  <div class="abs contact-item" style="left:832px">
    <span class="ic"><svg width="12" height="14" viewBox="0 0 24 28"><path fill="#fff" d="M12 0C6 0 1 5 1 11c0 8 11 17 11 17s11-9 11-17C23 5 18 0 12 0zm0 15a4 4 0 110-8 4 4 0 010 8z"/></svg></span>
    <div><b>Address</b><span>Los Angeles Centerline</span></div>
  </div>
</header>
<nav class="abs nav">
  <ul>
    <li class="active">HOME</li><li>COMPANY</li><li>OUR SERVICES</li><li>PROJECTS</li><li>BLOG</li><li>CONTACT US</li>
  </ul>
  <div class="tools"><i></i><i></i><i></i></div>
</nav>

<!-- hero -->
<section>
  <div class="abs hero-bg"></div>
  <div class="photo hero-photo" role="img" aria-label="Surveyor in hard hat and safety vest operating a total station on a tripod at a sandy site"></div>
  <div class="abs play" style="left:791px;top:324px"><svg width="16" height="18" viewBox="0 0 16 18"><path d="M0 0l16 9-16 9z" fill="#f08a24"/></svg></div>
  <h1 class="abs head hero-title">Land <em>Survey</em><br>Solutions</h1>
  <p class="abs" style="left:244px;top:360px;font-size:12px;color:#4a4d55">We provide land survey and digital mapping Services.</p>
  <div class="abs btn-dark" style="left:244px;top:408px;width:95px;height:32px">Read more</div>
</section>

<!-- services -->
<section>
  <div class="abs services-band"></div>
  <div class="abs eyebrow center" style="top:649px">Our Services</div>
  <h2 class="abs head center" style="top:664px;font-size:26px;color:var(--white)">Construction Services That<br>Exceed Expectations</h2>

  <article class="abs svc-card" style="left:244px">
    <div class="img" role="img" aria-label="Surveyor with instrument inside a tunnel"></div>
    <span class="badge"><svg width="18" height="18" viewBox="0 0 24 24" fill="none" stroke="#fff" stroke-width="2"><rect x="5" y="3" width="14" height="18"/><path d="M9 8h6M9 12h6M9 16h6"/></svg></span>
    <h3>Tunnel Survey</h3>
    <p>There are many construction project has the design has been completed available by the Professional</p>
    <a>READ MORE</a>
  </article>
  <article class="abs svc-card" style="left:487px">
    <div class="img" role="img" aria-label="Surveying tripod overlooking a city waterfront"></div>
    <span class="badge"><svg width="16" height="18" viewBox="0 0 24 28" fill="none" stroke="#fff" stroke-width="2.5"><path d="M12 2C7 2 3 6 3 11c0 7 9 15 9 15s9-8 9-15c0-5-4-9-9-9z"/><circle cx="12" cy="11" r="3"/></svg></span>
    <h3>3D City Mapping</h3>
    <p>There are many construction project has the design has been completed available by the Professional</p>
    <a>READ MORE</a>
  </article>
  <article class="abs svc-card" style="left:731px">
    <div class="img" role="img" aria-label="Surveyor taking measurements on a building site"></div>
    <span class="badge"><svg width="18" height="18" viewBox="0 0 24 24" fill="none" stroke="#fff" stroke-width="2"><path d="M3 21V9l9-6 9 6v12z"/><path d="M9 21v-6h6v6"/></svg></span>
    <h3>Cadastral &amp; Land Plan</h3>
    <p>There are many construction project has the design has been completed available by the Professional</p>
    <a>READ MORE</a>
  </article>

  <div class="abs" style="left:244px;top:1062px;width:712px;height:1px;background:var(--line)"></div>
  <div class="abs" style="left:588px;top:1050px;width:24px;height:24px;border-radius:50%;background:var(--red);color:#fff;font-size:15px;line-height:24px;text-align:center">+</div>
  <div class="abs center" style="top:1083px;font-size:8px;font-weight:500">Explore more services</div>
</section>

<!-- about -->
<section>
  <div class="abs eyebrow" style="left:256px;top:1171px">About Us</div>
  <h2 class="abs head" style="left:256px;top:1186px;font-size:26px">Constructing Your Future:<br>Reliable Building Services</h2>
  <p class="abs para" style="left:256px;top:1270px;width:330px">There are many variations of passages of Lorem Ipsum available, but the majority have suffered alteration in some form, by injected humour, or randomised words which don't look even slightly believable.</p>
  <div class="abs bar-label" style="top:1336px"><span>Industrial</span><span>87%</span></div>
  <div class="abs bar" style="top:1352px"><i style="width:87%"></i></div>
  <div class="abs bar-label" style="top:1372px"><span>Construction</span><span>54%</span></div>
  <div class="abs bar" style="top:1388px"><i style="width:54%"></i></div>
  <div class="abs bar-label" style="top:1411px"><span>Remodeling</span><span>24%</span></div>
  <div class="abs bar" style="top:1427px"><i style="width:24%"></i></div>
  <div class="abs btn-dark" style="left:256px;top:1465px;width:95px;height:29px">Read More</div>

  <div class="abs" style="left:640px;top:1214px;width:260px;height:256px">
    <span class="corner" style="left:0;top:0;border-left-width:2px;border-top-width:2px"></span>
    <span class="corner" style="right:0;top:0;border-right-width:2px;border-top-width:2px"></span>
    <span class="corner" style="left:0;bottom:0;border-left-width:2px;border-bottom-width:2px"></span>
    <span class="corner" style="right:0;bottom:0;border-right-width:2px;border-bottom-width:2px"></span>
  </div>
  <div class="photo" style="left:690px;top:1140px;width:160px;height:391px;background:linear-gradient(180deg,#f2f2f2 0%,#f08a24 25%,#e87a1c 45%,#3d4a5c 60%,#b9bec4 80%,#e0251b 100%);border-radius:40px 40px 4px 4px;opacity:.85" role="img" aria-label="Surveyor in orange overalls standing behind a total station tripod"></div>
</section>

<!-- why choose us -->
<section>
  <div class="photo" style="left:0;top:1542px;width:395px;height:459px;background:linear-gradient(160deg,#dfe4dc,#9aa46a 40%,#c6b84a 65%,#6f7a4c)" role="img" aria-label="Two surveyors in hi-vis vests using a total station in a grassy field"></div>
  <div class="abs" style="left:0;top:2001px;width:395px;height:102px;background:var(--navy)"></div>
  <div class="abs" style="left:13px;top:2010px;width:27px;height:72px;background:var(--red);color:#fff;font-size:7px;font-weight:600;writing-mode:vertical-rl;transform:rotate(180deg);text-align:center">PLAY NOW</div>
  <div class="photo" style="left:40px;top:2010px;width:158px;height:72px;background:linear-gradient(160deg,#4b5566,#2a3345)" role="img" aria-label="Video still of surveyors at work"></div>
  <div class="abs play" style="left:92px;top:2029px;width:32px;height:32px"><svg width="9" height="10" viewBox="0 0 16 18"><path d="M0 0l16 9-16 9z" fill="#e0251b"/></svg></div>
  <div class="abs" style="left:210px;top:2031px;font-size:12px;font-weight:500;color:#fff;line-height:1.5">How do we service provide<br>to our clients?</div>

  <div class="abs" style="left:395px;top:1573px;width:805px;height:530px;background:var(--gray)"></div>
  <div class="abs eyebrow" style="left:439px;top:1637px">Why Choose Us</div>
  <h2 class="abs head" style="left:439px;top:1652px;font-size:26px">Trusted Land Surveying Professionals</h2>
  <p class="abs para" style="left:439px;top:1700px;width:540px;font-size:9px">There are many variations of passages of Lorem Ipsum available, but the majority have suffered alteration in some form, by injected humour, or randomised words which don't look even slightly believable.</p>

  <div class="abs feature" style="left:439px;top:1774px">
    <svg width="30" height="36" viewBox="0 0 30 36" fill="none" stroke="#e0251b" stroke-width="1.5"><circle cx="15" cy="10" r="6"/><path d="M3 34V26c0-5 5-8 12-8s12 3 12 8v8z"/><path d="M9 6h12"/></svg>
    <h4 style="margin-top:8px">Client Satisfaction</h4>
    <p>We have Design a Interior Textures long and given to environment social and economic slightly believable.</p>
  </div>
  <div class="abs feature" style="left:710px;top:1774px">
    <svg width="30" height="36" viewBox="0 0 30 36" fill="none" stroke="#e0251b" stroke-width="1.5"><circle cx="15" cy="9" r="5"/><path d="M8 34l2-16h10l2 16M12 24h6M15 18v16"/></svg>
    <h4 style="margin-top:8px">Our Vision &amp; Mission</h4>
    <p>We have Design a Interior Textures long and given to environment social and economic slightly believable.</p>
  </div>
  <div class="abs feature" style="left:446px;top:1921px">
    <svg width="36" height="36" viewBox="0 0 36 36" fill="none" stroke="#e0251b" stroke-width="1.5"><rect x="3" y="8" width="28" height="24"/><path d="M3 26l10-10 6 6 12-14M24 4l8 8"/></svg>
    <h4 style="margin-top:8px">Project Planning</h4>
    <p>We have Design a Interior Textures long and given to environment social and economic slightly believable.</p>
  </div>
  <div class="abs feature" style="left:717px;top:1921px">
    <svg width="36" height="36" viewBox="0 0 36 36" fill="none" stroke="#e0251b" stroke-width="1.5"><path d="M3 14L18 4l15 10v20H3z"/><rect x="9" y="18" width="6" height="6"/><rect x="21" y="18" width="6" height="6"/><path d="M15 34v-6h6v6"/></svg>
    <h4 style="margin-top:8px">General Contraction</h4>
    <p>We have Design a Interior Textures long and given to environment social and economic slightly believable.</p>
  </div>
</section>

<!-- portfolio -->
<section>
  <div class="abs eyebrow center" style="top:2161px">Recent Portfolio</div>
  <h2 class="abs head center" style="top:2175px;font-size:26px">Explore Recent Projects</h2>
  <article class="abs proj" style="left:244px" role="img" aria-label="Road crew at a highway site">
    <h4>Highway Contract</h4><span>CONSTRUCTION</span></article>
  <article class="abs proj" style="left:487px" role="img" aria-label="Engineers reviewing plans at an apartment site">
    <h4>Apartment Design</h4><span>CONSTRUCTION</span></article>
  <article class="abs proj" style="left:731px" role="img" aria-label="Two engineers in hard hats on a railway project">
    <h4>Railway Construction</h4><span>COMMERCIAL</span></article>
  <div class="abs" style="left:586px;top:2522px;display:flex;gap:6px">
    <i style="width:6px;height:6px;border-radius:50%;background:var(--red);display:block"></i>
    <i style="width:6px;height:6px;border-radius:50%;background:#ddd;display:block"></i>
    <i style="width:6px;height:6px;border-radius:50%;background:#ddd;display:block"></i>
  </div>
</section>

<!-- stats -->
<section class="abs stats">
  <div class="abs stat" style="left:259px">
    <svg width="38" height="38" viewBox="0 0 38 38" fill="none" stroke="#fff" stroke-width="1.6"><circle cx="19" cy="12" r="6"/><path d="M6 36v-6c0-6 6-9 13-9s13 3 13 9v6z"/><path d="M11 8h16"/></svg>
    <div><b>857</b><span>Happy Clients</span></div>
  </div>
  <div class="abs stat" style="left:443px">
    <svg width="34" height="38" viewBox="0 0 34 38" fill="none" stroke="#fff" stroke-width="1.6"><rect x="4" y="4" width="26" height="32"/><path d="M10 12h14M10 18h14M10 24h14M10 30h8"/></svg>
    <div><b>380</b><span>Projects</span></div>
  </div>
  <div class="abs stat" style="left:614px">
    <svg width="38" height="38" viewBox="0 0 38 38" fill="none" stroke="#fff" stroke-width="1.6"><path d="M4 36V14h12V4h18v32z"/><path d="M9 20h3M9 26h3M21 10h3M27 10h3M21 18h3M27 18h3M21 26h3M27 26h3"/></svg>
    <div><b>955</b><span>Work Employed</span></div>
  </div>
  <div class="abs stat" style="left:792px">
    <svg width="38" height="38" viewBox="0 0 38 38" fill="none" stroke="#fff" stroke-width="1.6"><rect x="3" y="8" width="30" height="27"/><path d="M3 28l10-10 7 6 13-15M27 3l8 8"/></svg>
    <div><b>467</b><span>Planning Services</span></div>
  </div>
</section>

<!-- testimonial -->
<section>
  <div class="photo" style="left:0;top:2691px;width:1200px;height:309px;background:linear-gradient(90deg,#7e8a7a 0%,#c7cc8f 20%,#d9c9a8 38%,#f0ebe4 60%,#f7f5f2 100%)" role="img" aria-label="Surveyor looking through a red total station with a worker in the background"></div>
  <div class="abs" style="left:0;top:3000px;width:1200px;height:90px;background:var(--white)"></div>
  <div class="abs" style="left:651px;top:2744px;width:305px;height:324px;background:var(--white);box-shadow:0 8px 26px rgba(0,0,0,.08)"></div>
  <p class="abs" style="left:676px;top:2769px;width:260px;font-size:12.5px;font-weight:500;line-height:25px">I like more and more each day because it makes my life a lots of easier. They are the best and expertly trained team members who take the extra step and go the expert dynamic solutions to our customers fit changing global environment.</p>
  <div class="abs" style="left:676px;top:2985px;width:44px;height:44px;border-radius:50%;background:var(--gray);border:2px solid #ddd"></div>
  <div class="abs" style="left:687px;top:2996px;width:22px;height:22px;border-radius:50%;background:var(--red);color:#fff;font-family:Georgia,serif;font-size:16px;line-height:26px;text-align:center">“</div>
  <div class="abs" style="left:744px;top:2988px;font-size:11px;font-weight:600;white-space:nowrap">Owen Brisk <span style="font-size:8px;font-weight:400;color:var(--muted)">- fieldcrew - engineer</span></div>
  <div class="abs" style="left:744px;top:3007px;color:var(--red);font-size:11px;letter-spacing:2px">★★★★★</div>
  <div class="abs" style="left:921px;top:2997px;width:6px;height:6px;background:var(--red)"></div>

  <svg class="abs" style="left:244px;top:3030px" width="26" height="22" viewBox="0 0 26 22" fill="none" stroke="#e0251b" stroke-width="1.6"><path d="M3 14a10 10 0 0120 0"/><path d="M1 14h24v3H1zM13 4v6"/></svg>
  <div class="abs head" style="left:280px;top:3031px;font-size:17px">Hurry up! We're Hirring now</div>
  <div class="abs btn-dark" style="left:535px;top:3024px;width:85px;height:32px">Join now</div>
</section>

<!-- team -->
<section>
  <div class="abs eyebrow center" style="top:3157px">Our Team</div>
  <h2 class="abs head center" style="top:3171px;font-size:26px">Our Expert Team</h2>
  <div class="abs" style="left:0;top:3463px;width:1200px;height:62px;background:var(--gray)"></div>
  <article class="abs member" style="left:244px">
    <div class="img" role="img" aria-label="Team member in yellow hard hat on site"></div>
    <h4>Mara Ellison</h4><span>Financial Manager</span><i></i></article>
  <article class="abs member" style="left:487px">
    <div class="img" role="img" aria-label="Team member in orange hard hat and hi-vis vest"></div>
    <h4>Tobin Hale</h4><span>Menager</span><i></i></article>
  <article class="abs member" style="left:731px">
    <div class="img" role="img" aria-label="Team member in orange hard hat holding a tablet"></div>
    <h4>Rhea Calder</h4><span>Civil Engineer</span><i></i></article>
</section>

<!-- contact / faq -->
<section>
  <div class="abs eyebrow" style="left:256px;top:3589px">Contact Us</div>
  <h2 class="abs head" style="left:256px;top:3603px;font-size:26px">Have a any query?</h2>
  <div class="abs" style="left:256px;top:3667px;width:331px;height:134px;background:var(--navy)"></div>
  <div class="abs" style="left:256px;top:3667px;width:28px;height:134px;background:var(--red);color:#fff;font-size:8px;font-weight:600;writing-mode:vertical-rl;transform:rotate(180deg);text-align:center">CONTACT US</div>
  <div class="abs" style="left:341px;top:3704px;width:32px;height:32px;border-radius:50%;border:1.5px solid #fff;display:flex;align-items:center;justify-content:center">
    <svg width="14" height="14" viewBox="0 0 24 24"><path fill="#fff" d="M6.6 10.8c1.4 2.8 3.8 5.1 6.6 6.6l2.2-2.2c.3-.3.7-.4 1-.2 1.1.4 2.3.6 3.6.6.6 0 1 .4 1 1V20c0 .6-.4 1-1 1C10.6 21 3 13.4 3 4c0-.6.4-1 1-1h3.5c.6 0 1 .4 1 1 0 1.3.2 2.5.6 3.6.1.3 0 .7-.2 1l-2.3 2.2z"/></svg>
  </div>
  <div class="abs" style="left:389px;top:3700px;color:#cfd3da;font-size:8px">For any inquiries call now</div>
  <div class="abs" style="left:389px;top:3712px;color:#fff;font-size:19px;font-weight:500">0 555 014 228</div>

  <div class="abs faq open" style="top:3590px"><span>What Is The Qualification Of A Surveyor?</span><span class="mk">−</span></div>
  <p class="abs para" style="left:624px;top:3634px;width:310px;font-size:8.5px">There are many variations of passages of Lorem Ipsum available, but the majority have suffered alteration.</p>
  <div class="abs faq" style="top:3685px"><span>Who Is The Surveyor In Insurance?</span><span class="mk">+</span></div>
  <div class="abs faq" style="top:3731px"><span>What Is The Duty Of A Surveyor?</span><span class="mk">+</span></div>
  <div class="abs faq" style="top:3777px"><span>What Is A Land Surveyor's Job?</span><span class="mk">+</span></div>
</section>

<!-- blog -->
<section>
  <div class="abs eyebrow center" style="top:3878px">Recent Posts</div>
  <h2 class="abs head center" style="top:3892px;font-size:26px">Latest News &amp; Blog</h2>
  <article class="abs post" style="left:244px">
    <div class="img" role="img" aria-label="Total station on a tripod at a work site"></div>
    <div class="date">08<small>JUL</small></div>
    <h4>Exploring the World of Land Surveying</h4>
    <div class="meta"><svg width="8" height="8" viewBox="0 0 10 10" fill="none" stroke="#e0251b"><circle cx="5" cy="3" r="2"/><path d="M1 10c0-3 2-4 4-4s4 1 4 4"/></svg>fieldcrew<span class="gap"></span><svg width="8" height="8" viewBox="0 0 10 10" fill="none" stroke="#e0251b"><circle cx="5" cy="5" r="4"/></svg>Comments (1)</div></article>
  <article class="abs post" style="left:487px">
    <div class="img" role="img" aria-label="Worker in hi-vis vest under a steel structure"></div>
    <div class="date">08<small>JUL</small></div>
    <h4>Precision Matters in Every Land Survey</h4>
    <div class="meta"><svg width="8" height="8" viewBox="0 0 10 10" fill="none" stroke="#e0251b"><circle cx="5" cy="3" r="2"/><path d="M1 10c0-3 2-4 4-4s4 1 4 4"/></svg>fieldcrew<span class="gap"></span><svg width="8" height="8" viewBox="0 0 10 10" fill="none" stroke="#e0251b"><circle cx="5" cy="5" r="4"/></svg>Comments (0)</div></article>
  <article class="abs post" style="left:731px">
    <div class="img" role="img" aria-label="Surveyor in yellow vest near an excavator"></div>
    <div class="date">08<small>JUL</small></div>
    <h4>The Art of Professional Land Surveying</h4>
    <div class="meta"><svg width="8" height="8" viewBox="0 0 10 10" fill="none" stroke="#e0251b"><circle cx="5" cy="3" r="2"/><path d="M1 10c0-3 2-4 4-4s4 1 4 4"/></svg>fieldcrew<span class="gap"></span><svg width="8" height="8" viewBox="0 0 10 10" fill="none" stroke="#e0251b"><circle cx="5" cy="5" r="4"/></svg>Comments (0)</div></article>

  <div class="abs partner" style="left:280px"></div>
  <div class="abs partner" style="left:403px"></div>
  <div class="abs partner" style="left:518px;border-radius:50%"></div>
  <div class="abs partner" style="left:638px;border-radius:50%"></div>
  <div class="abs partner" style="left:759px"></div>
  <div class="abs partner" style="left:877px;border-radius:50%"></div>
</section>

<!-- footer -->
<footer class="abs footer">
  <div class="abs brand" style="left:244px;top:44px"><span class="dot"></span><span>VELMORA<small>LAND SURVEYING</small></span></div>
  <p class="abs" style="left:244px;top:97px;width:170px;font-size:8.5px;line-height:1.6;color:#cfd3da">We work to ensure people's com fort at their company specializing in house holance. During ourour</p>
  <div class="abs" style="left:244px;top:156px;font-size:20px;font-weight:500;color:var(--red)">555-014-22861</div>
  <div class="abs" style="left:244px;top:202px;width:139px;height:31px;border:1.5px solid #fff;font-size:7.5px;font-weight:500;display:flex;align-items:center;justify-content:center">REQUEST WITH ONLINE FORM</div>

  <h5 style="left:425px">Useful Links</h5>
  <ul class="flinks" style="left:425px"><li>Home</li><li>Offers</li><li>Locations</li><li>Services</li><li>Projects</li><li>Blog</li></ul>
  <ul class="flinks" style="left:510px"><li>About</li><li>Contact Us</li><li>Map</li><li>Faq</li><li>Pricing</li><li>Review</li></ul>

  <h5 style="left:608px">Recent Posts</h5>
  <div class="fpost" style="top:93px"><i role="img" aria-label="Survey post thumbnail"></i><div><b>Exploring the World of Land Surveying</b><span>JULY 8, 2024</span></div></div>
  <div class="fpost" style="top:157px"><i role="img" aria-label="Survey post thumbnail"></i><div><b>Precision Matters in Every Land Survey</b><span>JULY 8, 2024</span></div></div>
  <div class="fpost" style="top:221px"><i role="img" aria-label="Survey post thumbnail"></i><div><b>The Art of Professional Land Surveying</b><span>JULY 8, 2024</span></div></div>

  <h5 style="left:790px">Get In Touch</h5>
  <div class="finfo" style="top:93px"><svg class="pin" viewBox="0 0 24 28"><path fill="#e0251b" d="M12 0C6 0 1 5 1 11c0 8 11 17 11 17s11-9 11-17C23 5 18 0 12 0z"/></svg><span>Northgate Plaza HQ<br>88 Larkspur Ave., Los Angeles, USA</span></div>
  <div class="finfo" style="top:145px"><svg class="pin" viewBox="0 0 24 24"><rect x="2" y="5" width="20" height="14" fill="#e0251b"/></svg><span>Email : <b>info@velmoraland.com</b></span></div>
  <div class="finfo" style="top:198px"><svg class="pin" viewBox="0 0 24 24"><path fill="#e0251b" d="M6.6 10.8c1.4 2.8 3.8 5.1 6.6 6.6l2.2-2.2c.3-.3.7-.4 1-.2 1.1.4 2.3.6 3.6.6.6 0 1 .4 1 1V20c0 .6-.4 1-1 1C10.6 21 3 13.4 3 4c0-.6.4-1 1-1h3.5c.6 0 1 .4 1 1 0 1.3.2 2.5.6 3.6.1.3 0 .7-.2 1l-2.3 2.2z"/></svg><span>Phone : +12 (5) 550 0142<br>Support : +12 (5) 550 0142</span></div>

  <div class="abs" style="left:244px;top:320px;font-size:7.5px;color:#cfd3da">Developed and designed by Velmora</div>
</footer>

</body>
</html>
```